Quiet Harbor, LLC Business Card Design

We need a product business card designed for a new company Quiet Harbor, LLC. We make and resell waterless RV cleaner, polish and protectant. It cleans and protects in a simple spray and wipe step leaving the surface protected and conditioned to repel dust, dirt, water, smudges, bugs and fingerprints while preventing fogging. Safe on acrylic, plexiglas, lexan, plastic, rubber, painted surfaces, chrome, stainless, aluminum, vinyl, leather, glass.... This is an eco-friendly green product.

We want to play off the company name to tell the consumer that the product is easy to use and associate to the nostalgics 1950's in the USA... Thinking old travel trailer with hot rod truck pulling it as the graphic, maybe the husband cleaning the truck and the wife cleaning the trailer for a Quiet Harbor surface.
Updates

Just posted our newly finished logo. Need to have "Cleaner and Protectant" added to the design as well. Thanks everyone that has submitted thus far, i am working to get comments on all.

If you need a different file format, please let me know. Thank you.

Most important info, is the logo, website and the words "Cleaner" or "Clean" along "Protectant" or "Protect" the remainder is of less importance. Highlight: www.quietharborwash.example Focus is on company brand for Quieter Harbor Cleaner product: However, need a section for the following contact info: Walt Brinkley (xxx) xxx-xxxx email address Would like space for QR Code if possible.

Target Market(s)

Adults in the USA between ages of 35-75 that are actively involved in the Recreational Vehicle (RV), travel trailer, and hot rod lifestyle. We are targeting the RV marked of the high end travel, 5th wheel and bus RV market. Along with hot rods, automotive and motorcycle market.

Industry/Entity Type

Travel

Requirements
Must have
• Most important info, is the logo, website and the words "Cleaner" or "Clean" along "Protectant" or "Protect" the remainder is of less importance.

Highlight:
www.quietharborwash.example

Focus is on company brand for Quieter Harbor Cleaner product: However, need a section for the following contact info:

Walt Brinkley
(xxx) xxx-xxxx
email address
Nice to have
• Would like a space for a QR Code.

```html
<!DOCTYPE html>
<html lang="en">
<head>
<meta charset="utf-8">
<title>Quiet Harbor, LLC — Business Card</title>
<link href="https://fonts.googleapis.com/css2?family=Aldrich&display=swap" rel="stylesheet">
<style>
  :root {
    --page-bg: #e9e9ec;
    --card-white: #ffffff;
    --card-mist: #e4e5e8;
    --ink: #2b2b2f;
    --ink-soft: #4a4a50;
    --brand-blue: #3a3fae;
    --band-indigo: #3b3faf;
    --band-cyan: #21a6e6;
    --swoosh-grey: #8e8f95;
    --swoosh-blue: #2f4fc0;
    --on-band: #ffffff;
    --qr-space: #ffffff;
  }
  * { box-sizing: border-box; margin: 0; padding: 0; }
  html, body {
    width: 1200px; height: 900px; overflow: hidden;
    background: var(--page-bg);
    font-family: "Aldrich", "Segoe UI", sans-serif;
  }
  .card {
    position: absolute; left: 100px; top: 164px;
    width: 1000px; height: 572px;
    border-radius: 56px; overflow: hidden;
    background: radial-gradient(ellipse at 35% 35%, var(--card-white) 0%, var(--card-white) 40%, var(--card-mist) 100%);
    box-shadow: 0 18px 40px rgba(0,0,0,.18);
  }
  .card-waves { position: absolute; inset: 0; width: 100%; height: 100%; }
  .brand { position: absolute; left: 70px; top: 262px; }
  .brand-name {
    font-size: 58px; line-height: 1; font-weight: 400;
    color: var(--brand-blue); letter-spacing: 1px; text-transform: uppercase;
  }
  .brand-tagline {
    margin-top: 10px; font-size: 18px; letter-spacing: 3px;
    color: var(--ink-soft); text-transform: uppercase;
  }
  .holder { position: absolute; left: 560px; top: 48px; color: var(--ink); }
  .holder-name { font-size: 26px; letter-spacing: 1.5px; text-transform: uppercase; }
  .holder-role { font-size: 17px; color: var(--ink-soft); margin-top: 4px; padding-left: 12px; }
  .contact-list {
    position: absolute; left: 590px; top: 128px;
    list-style: none; color: var(--ink); font-size: 18px; letter-spacing: 1px;
  }
  .contact-list li { display: flex; align-items: center; gap: 12px; height: 31px; }
  .contact-list li.small { font-size: 15px; letter-spacing: .5px; }
  .contact-list svg { width: 18px; height: 18px; flex: none; }
  .address {
    position: absolute; left: 72px; top: 474px;
    color: var(--on-band); font-size: 24px; line-height: 1.4;
    letter-spacing: 1px; font-style: normal;
  }
  .qr-space {
    position: absolute; left: 846px; top: 420px;
    width: 104px; height: 104px; border-radius: 10px;
    background: var(--qr-space);
  }
</style>
</head>
<body>
  <section class="card" aria-label="Quiet Harbor business card">
    <svg class="card-waves" viewBox="0 0 1000 572" preserveAspectRatio="none" aria-hidden="true">
      <defs>
        <linearGradient id="bandGradient" x1="0" y1="0" x2="1" y2="0">
          <stop offset="0" stop-color="var(--band-indigo)"/>
          <stop offset="1" stop-color="var(--band-cyan)"/>
        </linearGradient>
        <linearGradient id="greySwoosh" x1="0" y1="0" x2="1" y2="0">
          <stop offset="0" stop-color="#c9c9cd"/>
          <stop offset=".5" stop-color="var(--swoosh-grey)"/>
          <stop offset="1" stop-color="#6d6e74"/>
        </linearGradient>
      </defs>
      <path d="M0,430 C250,360 520,420 720,372 C880,345 960,280 1000,170 L1000,196 C962,304 880,370 720,396 C520,444 250,388 0,458 Z" fill="url(#greySwoosh)"/>
      <path d="M720,400 C880,374 962,310 1000,206 L1000,226 C966,330 880,392 740,406 Z" fill="var(--swoosh-blue)"/>
      <path d="M0,478 C250,408 520,462 730,412 C885,388 966,336 1000,232 L1000,572 L0,572 Z" fill="url(#bandGradient)"/>
    </svg>

    <div class="brand">
      <h1 class="brand-name">Quiet Harbor</h1>
      <p class="brand-tagline">Cleaner &amp; Protectant</p>
    </div>

    <div class="holder">
      <p class="holder-name">Walt Brinkley</p>
      <p class="holder-role">Managing Director</p>
    </div>

    <ul class="contact-list">
      <li>
        <svg viewBox="0 0 24 24"><path d="M6.6 10.8a15 15 0 0 0 6.6 6.6l2.2-2.2a1 1 0 0 1 1-.25 11.4 11.4 0 0 0 3.6.57 1 1 0 0 1 1 1V20a1 1 0 0 1-1 1A17 17 0 0 1 3 4a1 1 0 0 1 1-1h3.5a1 1 0 0 1 1 1c0 1.25.2 2.45.57 3.57a1 1 0 0 1-.25 1z" fill="var(--ink)"/></svg>
        012 555 0147
      </li>
      <li>
        <svg viewBox="0 0 24 24"><rect x="6" y="2" width="12" height="20" rx="2" fill="none" stroke="var(--ink)" stroke-width="2"/><circle cx="12" cy="18" r="1.2" fill="var(--ink)"/></svg>
        012 555 0148
      </li>
      <li>
        <svg viewBox="0 0 24 24"><rect x="3" y="9" width="18" height="11" rx="1.5" fill="var(--ink)"/><rect x="7" y="3" width="10" height="7" fill="none" stroke="var(--ink)" stroke-width="2"/></svg>
        012 555 0149
      </li>
      <li class="small">
        <svg viewBox="0 0 24 24"><rect x="2" y="5" width="20" height="14" rx="1.5" fill="var(--ink)"/><path d="M3 6l9 7 9-7" fill="none" stroke="#fff" stroke-width="1.6"/></svg>
        hello@quietharbor.example
      </li>
      <li class="small">
        <svg viewBox="0 0 24 24"><circle cx="12" cy="12" r="9" fill="none" stroke="var(--ink)" stroke-width="1.8"/><path d="M3 12h18M12 3c3 3 3 15 0 18M12 3c-3 3-3 15 0 18" fill="none" stroke="var(--ink)" stroke-width="1.5"/></svg>
        www.quietharborwash.example
      </li>
    </ul>

    <address class="address">
      041.6th floor,Bay<br>Landing Road QHB
    </address>

    <div class="qr-space" role="img" aria-label="Space reserved for QR code"></div>
  </section>
</body>
</html>
```